Commercial Cleaning Company Website Design

We are working with Harbor Sweep Team. They are a commercial cleaning company that needs a new website design.

Some sites to use for inspiration:

https://www.plenvask.com
https://glint-panecleaning.com
https://tidyhelpers.net
https://calmnesthouse.com
https://www.thecleaningbureauxyz.com
https://www.dottiebroom.com

Thank you for taking the time to consider designing a website for us. We are web developers based in Stockton and Los Angeles, CA, USA. Most of our projects go through the same process. Understanding this process may help you win a project with us. We custom-code all of our websites in-house. We don’t have any requirements as to what tools you use for your design, but we prefer Figma files. For any design that we label as four-stars, we send it to the client for review. The client picks the final design they want us to use. Once we complete this process, we will continue to show additional clients all the four-star sites and purchase them later. Your designs will have multiple chances to sell. For better chances of success, we ask that you follow these guidelines.

IMAGES:
If you use any images or icons in the design, we ask that you have a link to the asset so we can purchase the image/icon. Most of the designs we submit do not have the customer’s images on them unless they have some great images. Be creative; show us the feeling you are trying to portray with your image choices. Use any royalty-free site you choose. We subscribe to Adobe and mainly use their images, but we can purchase images outside of Adobe.

PLEASE NOTE: we will not submit designs to clients with watermarks on the images.

FONTS:
We ask that you identify the fonts used in the design. This can be done in a message if you want. We typically use Google Fonts and Adobe Fonts.

CONTENT:
We're always open to different content and ideas. We often submit designs with stock images so the client can see our vision. We typically take pictures after the website launch to use their images with our vision. Lorem Ipsum is fine for paragraphs, but we ask that you write the headers in correct English. We want to be able to show the vision and identify the sections of the website.

INSPIRATION:
We typically add a couple of links in the brief of websites we like to help you get started in your design.

REVISIONS:
We do not often ask for revisions of the designs unless we see something in the design that may not appeal to the client. If there are slight changes that we want to make, we do that in the development process.

FEEDBACK:
We rarely give feedback on designs during the design process. We are working on many website projects and do not have the time to provide feedback. We usually respond if your request is well thought out and asks specific questions, but a note asking “feedback, please” usually goes unanswered.

```html
<!DOCTYPE html>
<html lang="en">
<head>
<meta charset="utf-8">
<title>Harbor Sweep Team — Commercial Cleaning</title>
<link href="https://fonts.googleapis.com/css2?family=Inter:wght@400;500;600;700&display=swap" rel="stylesheet">
<style>
:root{
  --teal:#13a297;
  --teal-dark:#0e8a80;
  --ink:#15172a;
  --text:#3b4150;
  --muted:#6b7280;
  --soft-bg:#f6f7f9;
  --card:#ffffff;
  --line:#e3e6ea;
  --navy:#0d4e8c;
  --navy-2:#0b3f74;
  --stat:#1c5e99;
  --footer:#141a33;
  --gold:#f5b50a;
}
*{box-sizing:border-box;margin:0;padding:0}
html,body{width:1200px;height:4803px;overflow:hidden}
body{font-family:"Inter",sans-serif;color:var(--text);background:#fff;position:relative}
.wrap{width:972px;margin:0 auto}
h2.section-title{font-size:33px;font-weight:600;color:var(--ink);text-align:center}
p.section-sub{font-size:14px;color:var(--muted);text-align:center;line-height:1.6;margin-top:20px}

/* header */
.site-header{height:75px;display:flex;align-items:center;justify-content:space-between;padding:0 117px 0 177px}
.brand{display:flex;align-items:center;gap:10px;font-weight:600;font-size:17px;color:var(--navy);letter-spacing:.5px}
.brand-dot{width:14px;height:14px;border-radius:50%;background:var(--teal)}
.main-nav{display:flex;align-items:center;gap:28px;font-size:13px;color:var(--ink);font-weight:500}
.btn{display:inline-flex;align-items:center;justify-content:center;gap:7px;border-radius:4px;font-weight:600;font-size:13px;color:#fff;background:var(--teal)}
.btn-nav{width:116px;height:41px;margin-left:10px}

/* hero */
.hero{height:512px;position:relative;background:linear-gradient(100deg,#2a2c2f 0%,#6b6a66 38%,#4a4b4c 62%,#141516 100%);text-align:center;color:#fff}
.hero::after{content:"";position:absolute;inset:0;background:rgba(10,12,16,.35)}
.hero-inner{position:relative;z-index:1;padding-top:136px}
.hero h1{font-size:46px;font-weight:600;line-height:1.16;letter-spacing:-.3px}
.hero p{font-size:15.5px;line-height:1.75;margin:28px auto 0;width:640px;color:#eef0f2}
.hero-actions{display:flex;justify-content:center;gap:14px;margin-top:36px}
.hero-actions .btn{height:43px;padding:0 24px}
.btn-ghost{background:rgba(255,255,255,.2);border:1px solid rgba(255,255,255,.35)}

/* services */
.services{background:var(--soft-bg);height:810px;padding-top:88px}
.card-grid{display:grid;grid-template-columns:repeat(3,307px);gap:24px;margin-top:44px}
.service-card{background:var(--card);height:266px;border-radius:6px;box-shadow:0 2px 10px rgba(20,30,50,.08);text-align:center;padding:46px 26px 0}
.service-card svg{width:40px;height:40px}
.service-card h3{font-size:19px;font-weight:500;color:var(--ink);margin-top:18px}
.service-card p{font-size:12.5px;color:var(--muted);line-height:1.75;margin-top:14px}

/* why */
.why{height:542px;padding-top:78px}
.why p.section-sub{width:570px;margin:22px auto 0}
.why-grid{display:grid;grid-template-columns:repeat(4,224px);gap:25px;margin-top:58px}
.why-card{height:268px;border-radius:6px;background:#fff;box-shadow:0 2px 10px rgba(20,30,50,.09);text-align:center;padding:38px 22px 0}
.why-card svg{width:36px;height:36px}
.why-card h3{font-size:18px;font-weight:500;color:var(--ink);margin-top:18px;line-height:1.45}
.why-card p{font-size:12.5px;color:var(--muted);line-height:1.75;margin-top:14px}

/* gallery */
.gallery{height:654px;padding-top:18px}
.gallery-grid{display:grid;grid-template-columns:repeat(3,313px);grid-auto-rows:212px;gap:15px 16px;margin-top:48px}
.photo{border-radius:5px}

/* testimonials */
.testimonials{background:var(--soft-bg);height:612px;padding-top:56px;overflow:hidden}
.t-track{display:flex;gap:24px;margin:60px 0 0 119px}
.t-card{flex:0 0 296px;height:348px;background:#fff;border-radius:6px;box-shadow:0 2px 10px rgba(20,30,50,.08);padding:30px 26px 0}
.stars{color:var(--gold);font-size:17px;letter-spacing:2px}
.t-card blockquote{font-style:italic;font-size:13px;line-height:1.75;color:var(--text);margin-top:16px}
.person{display:flex;align-items:center;gap:14px;margin-top:22px}
.avatar{width:46px;height:46px;border-radius:50%;background:linear-gradient(135deg,#c9b8a6,#6d5d52);border:2px solid var(--teal);flex:none}
.person strong{display:block;font-size:14px;font-weight:600;color:var(--ink)}
.person span{display:block;font-size:11px;color:var(--muted);line-height:1.6;margin-top:4px}

/* stats */
.stats{height:196px;display:flex;justify-content:center;gap:0;padding-top:60px}
.stat{width:152px;text-align:center}
.stat b{display:block;font-size:36px;font-weight:600;color:var(--stat)}
.stat span{display:block;font-size:12.5px;color:var(--muted);margin-top:10px}

/* cta */
.cta{margin:0 24px 0 19px;height:317px;border-radius:6px;background:linear-gradient(120deg,var(--navy) 0%,var(--navy-2) 100%);text-align:center;color:#fff;padding-top:74px}
.cta h2{font-size:30px;font-weight:600}
.cta p{font-size:15px;line-height:1.75;width:500px;margin:24px auto 0;color:#e6eef7}
.cta .btn{height:41px;width:282px;margin-top:22px}

/* quote */
.quote{position:relative;height:739px}
.quote-form{position:absolute;left:114px;top:56px;width:594px;height:627px;background:#fff;border-radius:6px;box-shadow:0 2px 10px rgba(20,30,50,.08);padding:38px 34px 0}
.quote-form h3{font-size:23px;font-weight:600;color:var(--ink)}
.field{margin-top:26px}
.quote-form h3 + .field{margin-top:34px}
.field label{display:block;font-size:11.5px;font-weight:500;color:var(--ink);margin-bottom:10px}
.field .input{height:38px;border:1px solid var(--line);border-radius:4px;padding:0 14px;display:flex;align-items:center;justify-content:space-between;font-size:13px;color:var(--muted)}
.field .select{color:var(--ink)}
.field .textarea{height:86px;align-items:flex-start;padding-top:12px;font-family:"Courier New",monospace;font-size:12px}
.btn-submit{width:100%;height:41px;margin-top:28px}
.contact-card{position:absolute;left:747px;top:56px;width:337px;height:448px;background:#fff;border-radius:6px;box-shadow:0 2px 10px rgba(20,30,50,.08);padding:34px 36px 0}
.contact-card h3{font-size:19px;font-weight:600;color:var(--ink)}
.info-row{display:flex;gap:14px;margin-top:22px}
.info-icon{width:28px;height:28px;border-radius:50%;background:var(--navy);flex:none;display:flex;align-items:center;justify-content:center;margin-top:8px}
.info-row strong{display:block;font-size:13px;font-weight:600;color:var(--ink)}
.info-row span{display:block;font-size:13px;line-height:1.6;margin-top:4px}
.zones{margin-top:30px}
.zones strong{font-size:13px;font-weight:600;color:var(--ink)}
.zones p{font-size:13px;line-height:1.6;margin-top:6px}
.map-alt{font-size:12.5px;margin-top:10px;color:var(--text)}

/* footer */
.site-footer{background:var(--footer);height:347px;color:#d5d9e6;position:relative;padding:22px 0 0 114px}
.foot-cols{display:flex}
.foot-col h4{font-size:14px;font-weight:600;color:#fff}
.foot-col ul{list-style:none;margin-top:20px}
.foot-col li{font-size:13px;margin-bottom:15px}
.foot-about{width:382px}
.foot-about p{font-size:13px;line-height:1.75;margin-top:20px;width:350px}
.socials{display:flex;gap:14px;margin-top:16px}
.socials span{width:32px;height:32px;border-radius:50%;background:rgba(255,255,255,.12)}
.foot-bottom{position:absolute;left:0;right:0;top:264px;text-align:center;font-size:11.5px}
.foot-bottom nav{display:flex;justify-content:center;gap:18px}
.foot-bottom small{display:block;font-size:10px;margin-top:22px;color:#aeb4c6}
</style>
</head>
<body>

<header class="site-header">
  <div class="brand"><span class="brand-dot"></span>Harbor Sweep Team</div>
  <nav class="main-nav">
    <span>Services</span><span>About</span><span>Gallery</span><span>Testimonials</span>
    <span class="btn btn-nav">Get a Quote</span>
  </nav>
</header>

<section class="hero" role="img" aria-label="Cleaner wiping an office window, darkened backdrop">
  <div class="hero-inner">
    <h1>Premium Commercial Cleaning<br>Solutions</h1>
    <p>Serving Stockton &amp; Los Angeles regions with licensed, insured teams — flexible scheduling and eco-friendly options.</p>
    <div class="hero-actions">
      <span class="btn"><svg width="12" height="12" viewBox="0 0 12 12"><rect x="1" y="2" width="10" height="9" rx="1" fill="#fff"/><rect x="3" y="0" width="1.5" height="3" fill="#fff"/><rect x="7.5" y="0" width="1.5" height="3" fill="#fff"/></svg>Request a Free Quote</span>
      <span class="btn btn-ghost"><svg width="12" height="12" viewBox="0 0 12 12"><rect x="1" y="1" width="10" height="10" rx="1" fill="#fff"/></svg>See Our Services</span>
    </div>
  </div>
</section>

<section class="services">
  <div class="wrap">
    <h2 class="section-title">Our Services</h2>
    <p class="section-sub">Comprehensive commercial cleaning services built for every facility type.</p>
    <div class="card-grid">
      <article class="service-card">
        <svg viewBox="0 0 40 40"><rect x="11" y="4" width="18" height="32" rx="2" fill="var(--teal)"/><g fill="#fff"><rect x="14" y="9" width="3" height="3"/><rect x="19" y="9" width="3" height="3"/><rect x="24" y="9" width="3" height="3" opacity="0"/><rect x="14" y="15" width="3" height="3"/><rect x="19" y="15" width="3" height="3"/><rect x="23" y="9" width="3" height="3"/><rect x="23" y="15" width="3" height="3"/><rect x="17" y="28" width="6" height="8"/></g></svg>
        <h3>Office Cleaning</h3>
        <p>Workstation sanitizing, trash removal, and break-room cleaning for productive workspaces.</p>
      </article>
      <article class="service-card">
        <svg viewBox="0 0 40 40"><path d="M4 14 20 5l16 9v21H4z" fill="var(--teal)"/><g fill="#fff"><rect x="10" y="17" width="20" height="3"/><rect x="10" y="22" width="20" height="3"/><rect x="10" y="27" width="20" height="3"/></g></svg>
        <h3>Warehouse Cleaning</h3>
        <p>Power washing, debris removal, and high-volume floor care for industrial spaces.</p>
      </article>
      <article class="service-card">
        <svg viewBox="0 0 40 40"><rect x="13" y="6" width="20" height="18" rx="3" fill="var(--teal)"/><rect x="7" y="14" width="20" height="20" rx="3" fill="var(--teal)" stroke="#fff" stroke-width="2"/><rect x="12" y="19" width="10" height="3" fill="#fff"/></svg>
        <h3>Window Cleaning</h3>
        <p>Interior &amp; exterior glass cleaning, storefronts, and high-rise windows for crystal clear views.</p>
      </article>
      <article class="service-card">
        <svg viewBox="0 0 40 40"><path d="M34 5 20 21" stroke="var(--teal)" stroke-width="3" stroke-linecap="round"/><path d="M17 19c4 1 6 4 5 7-4 6-12 8-18 7 3-3 4-6 5-10 2-3 5-4 8-4z" fill="var(--teal)"/></svg>
        <h3>Floor Care</h3>
        <p>Carpet cleaning, stripping, waxing, and polishing for high traffic areas that impress.</p>
      </article>
      <article class="service-card">
        <svg viewBox="0 0 40 40"><rect x="9" y="16" width="16" height="20" rx="3" fill="var(--teal)"/><rect x="13" y="9" width="8" height="7" fill="var(--teal)"/><circle cx="17" cy="27" r="3" fill="#fff"/><g fill="var(--teal)"><circle cx="28" cy="8" r="1.6"/><circle cx="33" cy="8" r="1.6"/><circle cx="28" cy="13" r="1.6"/><circle cx="33" cy="13" r="1.6"/><circle cx="30.5" cy="18" r="1.6"/></g></svg>
        <h3>Disinfection</h3>
        <p>Electrostatic, hospital-grade disinfecting for high-touch areas and peace of mind.</p>
      </article>
      <article class="service-card">
        <svg viewBox="0 0 40 40"><circle cx="15" cy="12" r="7" fill="var(--teal)"/><path d="M3 35c0-8 5-13 12-13s10 3 11 6v7z" fill="var(--teal)"/><circle cx="29" cy="28" r="7" fill="var(--teal)" stroke="#fff" stroke-width="2"/><path d="M29 24v4h3" stroke="#fff" stroke-width="2" fill="none"/></svg>
        <h3>Day Porter</h3>
        <p>Dedicated staff for restrooms, common areas, and quick-response cleaning throughout the day.</p>
      </article>
    </div>
  </div>
</section>

<section class="why">
  <div class="wrap">
    <h2 class="section-title">Why Choose Us</h2>
    <p class="section-sub">Licensed, insured, eco-friendly, flexible scheduling, and quality assurance you can trust.</p>
    <div class="why-grid">
      <article class="why-card">
        <svg viewBox="0 0 36 36"><path d="M18 3 31 8v9c0 8-6 14-13 16C11 31 5 25 5 17V8z" fill="var(--navy)"/><path d="M18 7v22c5-2 9-6 9-12V10z" fill="#fff"/></svg>
        <h3>Licensed &amp; Insured</h3>
        <p>Full coverage reduces facility risk and ensures professional standards.</p>
      </article>
      <article class="why-card">
        <svg viewBox="0 0 36 36"><path d="M31 5C15 5 7 12 8 26c13 1 22-7 23-21z" fill="var(--navy)"/><path d="M5 32c5-9 11-15 19-20" stroke="#fff" stroke-width="2" fill="none"/></svg>
        <h3>Green Cleaning</h3>
        <p>Eco-friendly and safe for staff, clients, and the environment.</p>
      </article>
      <article class="why-card">
        <svg viewBox="0 0 36 36"><rect x="4" y="7" width="28" height="26" rx="3" fill="var(--navy)"/><rect x="10" y="3" width="3" height="7" fill="var(--navy)"/><rect x="23" y="3" width="3" height="7" fill="var(--navy)"/><g fill="#fff"><rect x="8" y="16" width="4" height="4"/><rect x="16" y="16" width="4" height="4"/><rect x="24" y="16" width="4" height="4"/><rect x="8" y="24" width="4" height="4"/><rect x="16" y="24" width="4" height="4"/><rect x="24" y="24" width="4" height="4"/></g></svg>
        <h3>Flexible<br>Scheduling</h3>
        <p>Programs customized to your business hours with minimal disruption.</p>
      </article>
      <article class="why-card">
        <svg viewBox="0 0 36 36"><rect x="7" y="6" width="22" height="28" rx="3" fill="var(--navy)"/><rect x="13" y="3" width="10" height="6" rx="2" fill="var(--navy)" stroke="#fff" stroke-width="1.5"/><path d="M12 21l4 4 8-8" stroke="#fff" stroke-width="3" fill="none"/></svg>
        <h3>Quality Assurance</h3>
        <p>Inspections and service reports ensure consistently high standards.</p>
      </article>
    </div>
  </div>
</section>

<section class="gallery">
  <div class="wrap">
    <h2 class="section-title">Our Work Gallery</h2>
    <p class="section-sub">See examples of our commercial cleaning expertise across various industries.</p>
    <div class="gallery-grid">
      <div class="photo" role="img" aria-label="Cleaning team in uniforms and gloves in a bright office" style="background:linear-gradient(160deg,#e9ecef,#3c4a63)"></div>
      <div class="photo" role="img" aria-label="Cleaner wiping a window with a yellow cloth" style="background:linear-gradient(120deg,#5a6460,#9aa6a2 55%,#2c3431)"></div>
      <div class="photo" role="img" aria-label="Floor scrubbing machine in a large warehouse" style="background:linear-gradient(180deg,#cfd6d2,#8e9a93 60%,#b29b7a)"></div>
      <div class="photo" role="img" aria-label="Clean conference room with table and chairs" style="background:linear-gradient(150deg,#3d5c78,#a3a7a6 50%,#5a3e2a)"></div>
      <div class="photo" role="img" aria-label="Open office overlooking a city skyline" style="background:linear-gradient(180deg,#9bb5c4,#5d6d78 60%,#2b2f35)"></div>
      <div class="photo" role="img" aria-label="Small model house with keys on a wooden table" style="background:linear-gradient(150deg,#a9836a,#6e4a34 60%,#4a2f20)"></div>
    </div>
  </div>
</section>

<section class="testimonials">
  <h2 class="section-title">What Our Clients Say</h2>
  <p class="section-sub">Don't just take our word for it - hear from our satisfied clients.</p>
  <div class="t-track">
    <article class="t-card">
      <div class="stars">★★★★★</div>
      <blockquote>"Harbor Sweep Team transformed our office environment. Their attention to detail is exceptional, and their team is always professional and punctual. Our employees have noticed the difference and appreciate the cleaner workspace."</blockquote>
      <div class="person"><div class="avatar" role="img" aria-label="Client portrait"></div><div><strong>Dana Whitcombe</strong><span>Office Manager, Brightline Systems Inc.</span></div></div>
    </article>
    <article class="t-card">
      <div class="stars">★★★★★</div>
      <blockquote>"We've been using Harbor Sweep Team for over two years for our warehouse facility, and they consistently deliver exceptional service. Their ability to handle our large space while maintaining quality is impressive."</blockquote>
      <div class="person"><div class="avatar" role="img" aria-label="Client portrait"></div><div><strong>Luis Ferrand</strong><span>Facility Manager, Northgate Freight Co.</span></div></div>
    </article>
    <article class="t-card">
      <div class="stars">★★★★★</div>
      <blockquote>"The window cleaning service provided by Harbor Sweep Team exceeded our expectations. Our 15-story building now looks brand new, and the team completed the work efficiently with minimal disruption to our operations."</blockquote>
      <div class="person"><div class="avatar" role="img" aria-label="Client portrait"></div><div><strong>Priya Almont</strong><span>Property Manager, Crestview Holdings</span></div></div>
    </article>
    <article class="t-card"></article>
  </div>
</section>

<section class="stats">
  <div class="stat"><b>98%</b><span>Client Satisfaction</span></div>
  <div class="stat"><b>500+</b><span>Projects Completed</span></div>
  <div class="stat"><b>15+</b><span>Years Experience</span></div>
  <div class="stat"><b>24/7</b><span>Customer Support</span></div>
</section>

<section class="cta">
  <h2>Ready to Elevate Your Facility's Cleanliness?</h2>
  <p>Get a custom cleaning plan tailored to your specific needs and budget.</p>
  <span class="btn"><svg width="10" height="12" viewBox="0 0 10 12"><path d="M0 0h6l4 4v8H0z" fill="#fff"/></svg>Get Your Free Cleaning Proposal</span>
</section>

<section class="quote">
  <form class="quote-form">
    <h3>Request a Free Quote</h3>
    <div class="field"><label>Name / Company</label><div class="input">John Doe or Company XYZ</div></div>
    <div class="field"><label>Email</label><div class="input">you@company.com</div></div>
    <div class="field"><label>Phone</label><div class="input">(555) 014-2290</div></div>
    <div class="field"><label>Service of Interest</label><div class="input select">Office Cleaning<svg width="10" height="6" viewBox="0 0 10 6"><path d="M1 1l4 4 4-4" stroke="#222" stroke-width="1.5" fill="none"/></svg></div></div>
    <div class="field"><label>Additional Details</label><div class="input textarea">Square footage, frequency, start date, special requirements</div></div>
    <span class="btn btn-submit">Submit Request</span>
  </form>

  <aside class="contact-card">
    <h3>Contact Information</h3>
    <div class="info-row"><div class="info-icon"><svg width="12" height="14" viewBox="0 0 12 14"><path d="M6 0a5 5 0 0 1 5 5c0 4-5 9-5 9S1 9 1 5a5 5 0 0 1 5-5z" fill="#fff"/><circle cx="6" cy="5" r="2" fill="var(--navy)"/></svg></div><div><strong>Service Areas</strong><span>Serving greater Stockton &amp; Los Angeles regions</span></div></div>
    <div class="info-row"><div class="info-icon"><svg width="12" height="12" viewBox="0 0 12 12"><path d="M2 0l3 3-2 2c1 2 2 3 4 4l2-2 3 3-2 2C5 12 0 7 0 2z" fill="#fff"/></svg></div><div><strong>Phone</strong><span>(555) 014-2290</span></div></div>
    <div class="info-row"><div class="info-icon"><svg width="13" height="10" viewBox="0 0 13 10"><rect width="13" height="10" rx="1" fill="#fff"/><path d="M0 1l6.5 5L13 1" stroke="var(--navy)" fill="none"/></svg></div><div><strong>Email</strong><span>hello@harborsweepteam.com</span></div></div>
    <div class="info-row"><div class="info-icon"><svg width="13" height="13" viewBox="0 0 13 13"><circle cx="6.5" cy="6.5" r="6" fill="#fff"/><path d="M6.5 3v4h3" stroke="var(--navy)" stroke-width="1.4" fill="none"/></svg></div><div><strong>Business Hours</strong><span>Mon–Fri: 8am–6pm<br>Sat: 9am–1pm</span></div></div>
    <div class="zones"><strong>Service Zones</strong><p>Serving greater Stockton &amp; Los Angeles regions with licensed teams.</p><div class="map-alt">service area map</div></div>
  </aside>
</section>

<footer class="site-footer">
  <div class="foot-cols">
    <div class="foot-col foot-about">
      <h4>Harbor Sweep Team</h4>
      <p>Licensed &amp; Insured commercial cleaning services serving Stockton &amp; Los Angeles regions with premium cleaning solutions.</p>
      <div class="socials"><span></span><span></span><span></span><span></span></div>
    </div>
    <div class="foot-col" style="width:206px"><h4>Services</h4><ul><li>Office Cleaning</li><li>Warehouse Cleaning</li><li>Window Cleaning</li><li>Floor Care</li><li>Disinfection</li></ul></div>
    <div class="foot-col" style="width:209px"><h4>Company</h4><ul><li>About Us</li><li>Our Team</li><li>Careers</li><li>Blog</li><li>Contact</li></ul></div>
    <div class="foot-col"><h4>Support</h4><ul><li>FAQ</li><li>Privacy Policy</li><li>Terms &amp; Conditions</li><li>Service Areas</li><li>Get a Quote</li></ul></div>
  </div>
  <div class="foot-bottom">
    <nav><span>Privacy Policy</span><span>Terms &amp; Conditions</span><span>Sitemap</span></nav>
    <small>© 2025 Harbor Sweep Team. All Rights Reserved.</small>
  </div>
</footer>

</body>
</html>
```